Professionelles Design für Use Case Präsentationen im B2B-Bereich

Wir sind ein Schweizer Technologieunternehmen (Veltaro GmbH, www.veltaro-beispiel.ch), das datenbasierte Simulationen, Optimierung und Entscheidungsunterstützung für Unternehmen in Logistik, Produktion und Verkehr anbietet.
Ziel dieses Projekts ist es, bestehende Use Cases in ein modernes, visuell ansprechendes Format zu bringen, das unsere Kompetenz und den Nutzen für Kunden klar kommuniziert. Die Zielgruppe sind Entscheidungsträger in mittleren bis großen Industrieunternehmen (Bereichsleiter, Projektleiter, Geschäftsleitung).
Was wir brauchen:
– Ein cleanes, professionelles Design (PowerPoint oder PDF-Layout), das sich gut für Präsentationen, Whitepaper oder als LinkedIn-Content eignet.
– Klare Struktur mit Infografiken, Icons, Diagrammen oder Visualisierungen.
– Integration unseres Logos, Farbschemas und ggf. unseres Slogans.
Stilrichtung:
– Modern, technisch fundiert, aber nicht überladen
– Klar, direkt, seriös
– Gerne mit einem visuellen roten Faden (z. B. durchgängige Icons oder Layout-Struktur)
Ein Beispieldokument (UseCase Transportkosten) mit Inhalte ist angefügt. Ziel ist eine wiederverwendbare Vorlage, die wir für verschiedene Kunden-Use-Cases adaptieren können.
- Roboto

```html
<!DOCTYPE html>
<html lang="de">
<head>
<meta charset="utf-8">
<title>Use Case Transportkosten – Veltaro GmbH</title>
<link href="https://fonts.googleapis.com/css2?family=Roboto:wght@400;500;700;900&display=swap" rel="stylesheet">
<style>
:root{
  --page:#ffffff;
  --panel:#000000;
  --lime:#bccb72;
  --lime-text:#c6d47a;
  --ink:#141414;
  --white:#ffffff;
  --card-edge:#ffffff;
  --frame:#d9d9d9;
}
*{box-sizing:border-box;margin:0;padding:0}
html,body{width:880px;height:1200px;overflow:hidden;background:var(--page)}
body{font-family:"Roboto",sans-serif;position:relative;color:var(--white)}
.panel{position:absolute;left:63px;width:773px;background:var(--panel);overflow:hidden}
.panel--top{top:52px;height:547px}
.panel--bottom{top:622px;height:546px}
.brand-tab{position:absolute;background:var(--lime);display:flex;align-items:center;justify-content:center;gap:10px;color:var(--ink);font-weight:700}
.brand-tab--top{left:268px;top:0;width:237px;height:66px;border-radius:0 0 8px 8px;font-size:26px}
.brand-tab--bottom{left:302px;bottom:0;width:168px;height:45px;border-radius:8px 8px 0 0;font-size:19px}
.brand-dot{border-radius:50%;background:var(--ink)}
.brand-tab--top .brand-dot{width:30px;height:30px}
.brand-tab--bottom .brand-dot{width:22px;height:22px}
.headline{position:absolute;top:82px;left:0;width:100%;text-align:center;font-size:27px;font-weight:700}
.question{position:absolute;left:29px;top:133px;width:715px;height:37px;border-radius:10px;background:var(--lime);color:var(--ink);font-weight:700;font-size:19px;display:flex;align-items:center;justify-content:center}
.card{position:absolute;width:337px;height:149px;border:2px solid var(--card-edge);border-radius:28px;background:linear-gradient(160deg,#1a1a1a,#050505 60%);padding:12px 12px}
.card--benefit,.card--feedback{height:148px}
.card__head{display:flex;align-items:center;justify-content:center;gap:8px;height:34px;margin-bottom:10px}
.card__title{color:var(--lime-text);font-weight:700;font-size:17.5px;white-space:nowrap}
.card__body{font-size:11.8px;line-height:1.38;text-align:center;color:var(--white)}
.benefits{list-style:none;font-size:11.8px;line-height:1.38;padding-left:12px;margin-top:14px}
.benefits li{display:flex;align-items:center;gap:6px;white-space:nowrap}
.benefits svg{flex:none}
.card--situation{left:33px;top:195px}
.card--solution{left:403px;top:195px}
.card--benefit{left:33px;top:371px}
.card--feedback{left:403px;top:371px}
.card--feedback .card__body{margin-top:14px}
.shot-frame{position:absolute;border:4px solid var(--frame);border-radius:30px;background:#0a0a0a;padding:12px}
.shot-frame--map{left:32px;top:50px;width:343px;height:229px}
.shot-frame--report{left:377px;top:48px;width:363px;height:372px}
.shot{width:100%;height:100%;border-radius:10px}
.shot--map{background:linear-gradient(135deg,#d7e4c2,#e8ecd6 45%,#c9dcc4 70%,#b9d3e3)}
.shot--report{background:linear-gradient(180deg,#ffffff,#f2f4f6 40%,#e6ecef)}
.cta{position:absolute;left:33px;top:312px;width:340px;text-align:center}
.cta__kicker{color:var(--lime-text);font-size:25px;font-weight:700;line-height:1.2}
.cta__line{font-size:22px;font-weight:700;line-height:1.3}
.cta-rule{position:absolute;left:79px;top:419px;width:247px;height:4px;border-radius:2px;background:linear-gradient(90deg,#777,#fff,#777)}
.contact{position:absolute;display:flex;align-items:center;gap:10px;font-weight:700;white-space:nowrap}
.contact--phone{left:59px;top:485px;font-size:18px;letter-spacing:1.5px}
.contact--web{left:0;width:100%;justify-content:center;top:464px;font-size:16px;letter-spacing:1px}
.contact--mail{left:507px;top:485px;font-size:15px;letter-spacing:.5px}
.pointer{position:absolute;top:488px}
.pointer--left{left:284px}
.pointer--right{left:475px}
</style>
</head>
<body>

<section class="panel panel--top">
  <div class="brand-tab brand-tab--top"><span class="brand-dot"></span>Veltaro</div>
  <h1 class="headline">Was wäre, wenn…</h1>
  <p class="question">…Sie neue Standorte mit echten Transportkosten vergleichen könnten?</p>

  <article class="card card--situation">
    <div class="card__head">
      <svg width="32" height="32" viewBox="0 0 34 34" fill="none" stroke="#fff" stroke-width="1.6"><path d="M5 6h8l-2 3 2 3H5z"/><path d="M5 6v24M12 18h14v12H12zM16 22h2M20 22h2M16 26h2M20 26h2"/></svg>
      <h2 class="card__title">Ausgangslage &amp; Ziel</h2>
    </div>
    <p class="card__body">Ein Handelsunternehmen prüfte mehrere neue Standorte. Dabei ging es um die Frage: Wie verändern sich die Transportkosten und die Kundenbelieferung bei einem Umzug?</p>
  </article>

  <article class="card card--solution">
    <div class="card__head">
      <svg width="30" height="32" viewBox="0 0 34 34" fill="none" stroke="#fff" stroke-width="1.6"><circle cx="17" cy="11" r="6"/><path d="M15 17v3h4v-3M4 24h8l6 3 10-5-2-2-8 3"/><path d="M17 2v1M9 5l1 1M25 5l-1 1"/></svg>
      <h2 class="card__title">Die Lösung – Unsere Simulation</h2>
    </div>
    <p class="card__body">Wir kombinierten Standortdaten, Kundenadressen und Liefermengen mit einem automatisierten Tourenplaner. So wurden die neuen Transportkosten und Fahrzeiten für alle Varianten berechnet und visualisiert.</p>
  </article>

  <article class="card card--benefit">
    <div class="card__head">
      <svg width="32" height="32" viewBox="0 0 34 34" fill="none" stroke="#fff" stroke-width="1.6"><circle cx="18" cy="15" r="6"/><path d="M18 12v6M16 13.5h3.5M16 16.5h3.5M4 26h8l6 3 12-5-2-2-9 3M9 6v6M6 9h6M27 4v6M24 7h6"/></svg>
      <h2 class="card__title">Der konkrete Nutzen</h2>
    </div>
    <ul class="benefits">
      <li><svg width="11" height="11" viewBox="0 0 12 12" fill="none" stroke="#fff"><circle cx="6" cy="6" r="5"/><path d="M3.5 6l2 2 3-4"/></svg>Vergleich der Standorte mit echten Touren</li>
      <li><svg width="11" height="11" viewBox="0 0 12 12" fill="none" stroke="#fff"><circle cx="6" cy="6" r="5"/><path d="M3.5 6l2 2 3-4"/></svg>Transparente Berechnung der Transportkosten</li>
      <li><svg width="11" height="11" viewBox="0 0 12 12" fill="none" stroke="#fff"><circle cx="6" cy="6" r="5"/><path d="M3.5 6l2 2 3-4"/></svg>Klare Entscheidungsgrundlage für Geschäftsleitung</li>
      <li><svg width="11" height="11" viewBox="0 0 12 12" fill="none" stroke="#fff"><circle cx="6" cy="6" r="5"/><path d="M3.5 6l2 2 3-4"/></svg>Erste Resultate in weniger als 3 Wochen</li>
    </ul>
  </article>

  <article class="card card--feedback">
    <div class="card__head">
      <svg width="34" height="32" viewBox="0 0 36 34" fill="none" stroke="#fff" stroke-width="1.6"><rect x="3" y="8" width="16" height="12" rx="2"/><path d="M7 20v4l4-4"/><circle cx="8" cy="14" r="1"/><circle cx="11" cy="14" r="1"/><circle cx="14" cy="14" r="1"/><path d="M26 14c-3-4-8 0-4 4l4 4 4-4c4-4-1-8-4-4z"/></svg>
      <h2 class="card__title" style="margin-left:22px">Kundenfeedback</h2>
    </div>
    <p class="card__body">“Wir wussten genau, welcher Standort für unsere Kundenbelieferung am effizientesten ist – datenbasiert und nachvollziehbar.”</p>
  </article>
</section>

<section class="panel panel--bottom">
  <div class="shot-frame shot-frame--map">
    <div class="shot shot--map" role="img" aria-label="Kartenansicht der Schweiz mit Standorten und Kundenadressen als farbige Punkte"></div>
  </div>
  <div class="shot-frame shot-frame--report">
    <div class="shot shot--report" role="img" aria-label="Auswertung einer Beispiel-Tourenplanung mit Kennzahlen, Tourenkarte, Tabelle und Balkendiagrammen"></div>
  </div>

  <div class="cta">
    <p class="cta__kicker">Jetzt testen:</p>
    <p class="cta__line">Standortentscheidung</p>
    <p class="cta__line">absichern mit Simulation</p>
  </div>
  <div class="cta-rule"></div>

  <p class="contact contact--web">www.veltaro-beispiel.ch</p>
  <p class="contact contact--phone">
    <svg width="26" height="26" viewBox="0 0 26 26" fill="none" stroke="#bccb72" stroke-width="1.8"><path d="M6 3l4 5-2 3c1 3 4 6 7 7l3-2 5 4-3 4C11 24 2 15 2 6z"/><path d="M15 6a6 6 0 0 1 5 5M15 2a10 10 0 0 1 9 9"/></svg>
    +41 44 210 35 80
  </p>
  <svg class="pointer pointer--left" width="18" height="18" viewBox="0 0 20 20"><path d="M18 2L2 9l7 2 2 7z" fill="#bccb72"/></svg>
  <svg class="pointer pointer--right" width="18" height="18" viewBox="0 0 20 20"><path d="M2 2l16 7-7 2-2 7z" fill="#bccb72"/></svg>
  <p class="contact contact--mail">
    <svg width="24" height="24" viewBox="0 0 26 26" fill="none" stroke="#bccb72" stroke-width="1.8"><rect x="3" y="7" width="20" height="15" rx="2"/><path d="M3 9l10 7 10-7M7 7V3h12v4"/></svg>
    info@veltaro-beispiel.ch
  </p>

  <div class="brand-tab brand-tab--bottom"><span class="brand-dot"></span>Veltaro</div>
</section>

</body>
</html>
```